Business Card Design

Plumbing business.
Looking for a simple but professional looking design.
There are two variations of the logo; white background and black background. The logo with the white background is the primary business logo.
Industry/Entity Type
Business
Contact Information for Business Card
Marcus Fenley
Owner/Licensed Plumber
0412 639 718
info@marcusfenleyplumbing.com.au
www.marcusfenleyplumbing.com.au
Lic. 63914

```html
<!DOCTYPE html>
<html lang="en">
<head>
<meta charset="utf-8">
<title>Marcus Fenley Plumbing – Business Card</title>
<link rel="stylesheet" href="https://fonts.googleapis.com/css2?family=Open+Sans:wght@400;700&display=swap">
<style>
  :root {
    --backdrop: #262626;
    --teal: #1fa4b1;
    --card-white: #f1f1f1;
    --text-grey: #4a4a4a;
    --photo-light: #e9e9e9;
    --photo-mid: #dcdcdc;
    --white: #ffffff;
  }
  * { margin: 0; padding: 0; box-sizing: border-box; }
  html, body {
    width: 1200px;
    height: 900px;
    overflow: hidden;
    background: var(--backdrop);
    font-family: "Open Sans", Arial, sans-serif;
  }
  .stage { position: relative; width: 1200px; height: 900px; }

  /* Front of card */
  .card-front {
    position: absolute;
    left: 215px;
    top: 150px;
    width: 550px;
    height: 345px;
    background: var(--teal);
    box-shadow: 0 10px 30px rgba(0,0,0,.5);
  }
  .brand {
    position: absolute;
    left: 95px;
    top: 105px;
    display: flex;
    align-items: center;
    gap: 24px;
  }
  .brand-square {
    width: 92px;
    height: 92px;
    background: var(--white);
  }
  .brand-name {
    color: var(--white);
    font-weight: 700;
    font-size: 40px;
    line-height: 1.05;
    letter-spacing: 1px;
    text-transform: uppercase;
  }

  /* Back of card */
  .card-back {
    position: absolute;
    left: 432px;
    top: 415px;
    width: 530px;
    height: 305px;
    background: var(--card-white);
    box-shadow: 0 10px 30px rgba(0,0,0,.5);
    overflow: hidden;
  }
  .card-back-band {
    position: absolute;
    left: 0; top: 0;
    width: 18px;
    height: 100%;
    background: var(--teal);
  }
  .card-back-photo {
    position: absolute;
    left: 120px;
    top: 30px;
    width: 260px;
    height: 275px;
    background: radial-gradient(ellipse at 50% 45%, var(--photo-mid) 0%, var(--photo-light) 70%, transparent 100%);
  }
  .contact {
    position: absolute;
    left: 40px;
    top: 16px;
    color: var(--text-grey);
  }
  .contact-name {
    color: var(--teal);
    font-weight: 700;
    font-size: 34px;
    line-height: 1.05;
    text-transform: uppercase;
  }
  .contact-role {
    font-size: 15px;
    text-transform: uppercase;
    margin-bottom: 14px;
  }
  .contact-phone {
    color: var(--teal);
    font-size: 19px;
    line-height: 1.3;
  }
  .contact-line {
    font-size: 19px;
    line-height: 1.3;
  }
  .contact-licence {
    font-size: 14px;
    margin-top: 4px;
    text-transform: uppercase;
  }
</style>
</head>
<body>
<main class="stage">
  <section class="card-front">
    <div class="brand">
      <div class="brand-square"></div>
      <div class="brand-name">Marcus Fenley<br>Plumbing</div>
    </div>
  </section>

  <section class="card-back">
    <div class="card-back-photo" role="img" aria-label="Faint greyscale photo of a toilet in a bathroom"></div>
    <div class="card-back-band"></div>
    <div class="contact">
      <h1 class="contact-name">Marcus Fenley</h1>
      <p class="contact-role">Owner/Licensed Plumber</p>
      <p class="contact-phone">0412 639 718</p>
      <p class="contact-line">info@marcusfenleyplumbing.com.au</p>
      <p class="contact-line">www.marcusfenleyplumbing.com.au</p>
      <p class="contact-licence">Lic. 63914</p>
    </div>
  </section>
</main>
</body>
</html>
```